The next stage in our 106 year history in Specialised Stationery

We need a business card design(which is also adaptable for our general stationery) to suit the changing face of our business. Brevik, an Australian company has been the leader in its category since 1907. We design and print various books required by small business to comply with government legislation in regards to keeping records. Accountancy, Payroll, Vehicle usage recording, Firearms registration etc. The Brevik logo a blue diamond is one of the best known in our industry. As manual recording has declined in the last few years we have diversified into other areas: Safety Apparel, Personal Protective Equipment (PPE) and web based software for bookkeeping and Customer Relationship management(CRM). Separate logos have been adopted for each of these being: Brevik Systems, Brevik Safety, Brevik Apparel and Brevik Software each with same diamond but different colour background. This has made it easy to identify the different sectors but difficult to bring together for a Corporate identity in Business cards etc. We are looking to bring all logos together (not one logo) but still allow the logo to depict the diversity of our offering, while still being able to have a category specific logo for each of the divisions. All products go through the same distribution channel, Office Products. The final design should depict an old established company well, known and trusted but leaping forward and still retaining same values they have come to trust.

Target Market(s)

Micro to small business companies generally who employ 20 or less people.

Industry/Entity Type

Small Business

Requirements
Must have
• The diamonds are well recognised and the new design should retain the integrity of them.

```html
<!DOCTYPE html>
<html lang="en">
<head>
<meta charset="utf-8">
<title>Brevik Business Cards</title>
<link rel="stylesheet" href="https://fonts.googleapis.com/css2?family=Arimo:wght@400;700&display=swap">
<style>
  :root {
    --backdrop: #6c91b6;
    --card-white: #ffffff;
    --pattern-grey: #e6e6e6;
    --brand-blue: #0070b8;
    --ink: #111111;
    --web-grey: #a8a8a8;
  }
  html, body {
    margin: 0;
    padding: 0;
    width: 1200px;
    height: 1000px;
    overflow: hidden;
    background: var(--backdrop);
    font-family: "Arimo", Arial, sans-serif;
  }
  .canvas { position: relative; width: 1200px; height: 1000px; }
  .card { position: absolute; display: block; }
  .card-front { left: 150px; top: 80px; width: 555px; height: 318px; }
  .card-back { left: 32px; top: 597px; width: 505px; height: 297px; }
  .card-contact { left: 587px; top: 417px; width: 555px; height: 318px; }
  .wordmark { font-family: "Arimo", Arial, sans-serif; font-weight: 700; fill: var(--brand-blue); }
  .person-name { font-weight: 700; fill: var(--ink); font-size: 40px; }
  .person-role { fill: var(--ink); font-size: 26px; }
  .contact-line { fill: var(--ink); font-size: 23px; }
  .web-address { fill: var(--web-grey); font-size: 26px; }
  .division-list { fill: var(--card-white); font-weight: 700; font-size: 22px; letter-spacing: 0.3px; }
  svg text { font-family: "Arimo", Arial, sans-serif; }
</style>
</head>
<body>
<main class="canvas">

  <!-- Front of card: brand side -->
  <svg class="card card-front" viewBox="0 0 555 318" aria-label="Brevik card front">
    <rect class="lattice-fill" width="555" height="318" fill="var(--pattern-grey)" role="img" aria-label="Light grey diamond lattice background pattern"/>
    <rect x="212" y="96" width="22" height="22" fill="var(--brand-blue)"/>
    <text class="wordmark" x="244" y="117" font-size="28">Brevik</text>
    <rect y="212" width="555" height="5" fill="var(--brand-blue)"/>
    <rect y="217" width="555" height="11" fill="var(--card-white)"/>
    <rect y="228" width="555" height="20" fill="var(--brand-blue)"/>
    <text class="wordmark" x="277" y="300" font-size="44" text-anchor="middle">BREVIK</text>
  </svg>

  <!-- Back of card: large brand mark area -->
  <svg class="card card-back" viewBox="0 0 505 297" aria-label="Brevik card back">
    <rect width="505" height="297" fill="var(--pattern-grey)"/>
    <rect x="118" y="124" width="44" height="44" fill="var(--brand-blue)"/>
    <text class="wordmark" x="178" y="164" font-size="56">Brevik</text>
  </svg>

  <!-- Contact side -->
  <svg class="card card-contact" viewBox="0 0 555 318" aria-label="Brevik contact card">
    <rect width="555" height="318" fill="var(--card-white)"/>
    <polygon class="lattice-corner" points="253,0 555,0 555,183" fill="var(--pattern-grey)" role="img" aria-label="Diamond lattice pattern in the top right corner"/>
    <text class="person-name" x="41" y="85">Alan Porter</text>
    <text class="person-role" x="93" y="112">President</text>
    <text class="contact-line" x="104" y="179">Email: alan.porter@brevik.com</text>
    <text class="contact-line" x="104" y="211">Tel: 555 014</text>
    <text class="web-address" x="550" y="260" text-anchor="end">www.brevik.com</text>
    <rect y="268" width="555" height="35" fill="var(--brand-blue)"/>
    <text class="division-list" x="277" y="294" text-anchor="middle">SYSTEMS | SAFETY | SOFTWARE | APPAREL</text>
  </svg>

</main>
</body>
</html>
```